Q-VARO one-page Handout infographic for software product

We need a single page info-graphic designed that matches our branding and communicates how our software is easy to use and get started with. It's the first piece of content we want to hand someone when they say "What does your software do?" or a salesman can drop at a perspective clients office as a leave-behind. Our product is a very complex manufacturing simulation software that has a tremendous amount of features and functionality that can overwhelm a customer at first glance. it is primarily used by sheet metal stamping companies that produce automotive, appliance, and aerospace parts. We want to accomplish two things with this piece of marketing. 1. Show how simple the process of getting started is and 2. give the basic rundown of what it is and its features. Our main differentiators are we are long established (22) years in business, and our software is the most capable in the industry. i would envision this being a single page with infographic (and some details) on one side and more detail and features on the other.

Target Market(s)

Metal stamping companies and their suppliers

Industry/Entity Type

Manufaturing - specifically Metal stamping companies that make automotive and appliance parts

Font styles to use
Sans Serif

Colors
0054AA
0677BA
7BADD7
CADEEF
E8F1F8
0094D4
00A9DD
6FCCEA
C7EBF8
E9F6FB
FFF300
FFF600
FEFA6F
FFFEC7
FFFEE8
FFC000
F8CF3A
FAE287
FDF2CF
FEFAEE

Requirements
Must have
• Clean professional look, we are a tech company and need to look very polished
Nice to have
• Good branding with our logo - try to use same color pallet as the logo

```html
<!DOCTYPE html>
<html lang="en">
<head>
<meta charset="utf-8">
<title>Q-VARO Handout</title>
<link href="https://fonts.googleapis.com/css2?family=Montserrat:wght@400;500;600;700;800&display=swap" rel="stylesheet">
<style>
  :root{
    --stage:#0f2c42;
    --teal:#1d5b73;
    --teal-mid:#4a8293;
    --grey:#5a5a5a;
    --ink:#1f1f1f;
    --yellow:#fcc419;
    --paper:#f3f4f6;
    --white:#ffffff;
  }
  *{box-sizing:border-box;margin:0;padding:0}
  html,body{width:1200px;height:1200px;overflow:hidden;background:var(--stage);font-family:'Montserrat',sans-serif;color:var(--ink)}
  .page{position:absolute;top:248px;width:503px;height:704px;background:linear-gradient(160deg,#f7f8f9,#eceef0 55%,#f6f7f8);overflow:hidden}
  .page--process{left:76px}
  .page--details{left:628px}
  .page__header{position:absolute;left:0;top:0;width:100%;height:94px;background:var(--white)}
  .page__rule{position:absolute;left:0;top:94px;width:100%;height:8px;background:var(--teal)}
  .page__foot{position:absolute;left:0;bottom:0;width:100%;height:48px;background:var(--yellow)}
  .brand{position:absolute;left:17px;top:32px;display:flex;align-items:center;gap:8px}
  .brand__mark{width:30px;height:40px;background:var(--yellow)}
  .brand__name{font-weight:800;font-size:34px;color:var(--teal);letter-spacing:1px;line-height:1}
  .title-band{position:absolute;top:32px;right:0;height:37px;background:var(--yellow);color:var(--white);font-weight:700;font-size:21px;display:flex;align-items:center;padding-left:14px}
  .page--process .title-band{left:242px}
  .page--details .title-band{left:271px;padding-left:17px}
  .abs{position:absolute}
  .step-label{position:absolute;top:131px;width:100px;margin-left:-50px;text-align:center;font-size:12px;line-height:15px}
  .panel{position:absolute;left:27px;top:271px;width:447px;height:306px;border:1px solid #555;background:var(--white)}
  .panel__head{height:25px;background:var(--teal);color:var(--white);font-weight:700;font-size:14px;display:flex;align-items:center;justify-content:center}
  .hl{color:var(--yellow)}
  .step-row{position:absolute;left:31px;width:410px;height:78px;display:flex;align-items:center}
  .step-row__num{width:58px;height:78px;background:var(--yellow);color:var(--white);font-weight:800;font-size:92px;line-height:78px;text-align:center;overflow:hidden}
  .step-row__text{position:absolute;left:98px;font-size:12px;line-height:15px;padding-right:20px}
  .note{position:absolute;left:40px;top:585px;width:424px;height:15px;background:var(--teal);color:var(--white);font-size:10px;display:flex;align-items:center;justify-content:center;box-shadow:0 1px 3px rgba(0,0,0,.3)}
  .features{position:absolute;left:41px;top:134px;width:423px;height:198px;border:1px solid #555;background:var(--white)}
  .features__head{height:25px;background:var(--teal);color:var(--white);font-weight:700;font-size:14px;display:flex;align-items:center;justify-content:center}
  .features__list{list-style:none;padding:9px 10px 0 30px}
  .features__list li{position:relative;font-size:10.3px;line-height:13.5px;margin-bottom:5px}
  .features__list li::before{content:"";position:absolute;left:-16px;top:3px;width:8px;height:7px;background:linear-gradient(90deg,var(--yellow) 35%,var(--teal) 35%)}
  .guarantee{position:absolute;left:73px;top:356px;width:395px;height:44px;background:var(--teal);color:var(--white);font-size:10px;line-height:13px;padding:8px 10px 0 22px}
  .guarantee b{color:var(--yellow);font-weight:700}
  .shield{position:absolute;left:35px;top:342px}
  .promise{position:absolute;left:124px;top:414px;width:257px;height:23px;background:var(--yellow);color:var(--white);font-size:14px;display:flex;align-items:center;justify-content:center;box-shadow:0 1px 3px rgba(0,0,0,.25)}
  .contact-head{position:absolute;left:147px;top:480px;width:216px;height:25px;background:var(--teal);color:var(--white);font-weight:700;font-size:15px;display:flex;align-items:center;justify-content:center}
  .contact-name{position:absolute;left:0;width:100%;top:517px;text-align:center;font-weight:700;font-size:12px;padding-left:0}
  .contact-line{position:absolute;left:189px;display:flex;align-items:center;gap:8px;font-size:10.5px}
  .contact-line__icon{width:12px;height:12px;background:var(--yellow);display:flex;align-items:center;justify-content:center}
</style>
</head>
<body>

<section class="page page--process">
  <div class="page__header">
    <div class="brand"><span class="brand__mark"></span><span class="brand__name">Q-VARO</span></div>
    <div class="title-band">Process Simplification</div>
  </div>
  <div class="page__rule"></div>

  <div class="step-label" style="left:68px">Get<br>Q-VARO</div>
  <div class="step-label" style="left:159px">Add<br>Equipment</div>
  <div class="step-label" style="left:250px">Verify<br>Equipment</div>
  <div class="step-label" style="left:342px">Optimize<br>all Projects</div>
  <div class="step-label" style="left:432px">Repeat for each<br>press line</div>

  <svg class="abs" style="left:0;top:160px" width="503" height="100" viewBox="0 160 503 100">
    <polygon points="23,166 108,166 112,171 108,176 23,176 27,171" fill="#fcc419"/>
    <polygon points="114,166 199,166 203,171 199,176 114,176 118,171" fill="#1d5b73"/>
    <polygon points="205,166 290,166 294,171 290,176 205,176 209,171" fill="#4a8293"/>
    <polygon points="296,166 381,166 385,171 381,176 296,176 300,171" fill="#5a5a5a"/>
    <polygon points="387,166 472,166 476,171 472,176 387,176 391,171" fill="#222"/>
    <g fill="#fff"><circle cx="68" cy="171" r="2"/><circle cx="159" cy="171" r="2"/><circle cx="250" cy="171" r="2"/><circle cx="342" cy="171" r="2"/><circle cx="433" cy="171" r="2"/></g>
    <g stroke-width="1"><line x1="68" y1="174" x2="68" y2="206" stroke="#fcc419"/><line x1="159" y1="174" x2="159" y2="206" stroke="#1d5b73"/><line x1="250" y1="174" x2="250" y2="206" stroke="#4a8293"/><line x1="342" y1="174" x2="342" y2="206" stroke="#5a5a5a"/><line x1="433" y1="174" x2="433" y2="206" stroke="#222"/></g>
    <!-- get -->
    <circle cx="68" cy="227" r="21" fill="#fff" stroke="#fcc419" stroke-width="1.5"/>
    <path d="M68 214v12M63 221l5 5 5-5" stroke="#fcc419" stroke-width="2.5" fill="none"/>
    <path d="M55 228q3 8 13 10q10-2 13-10" stroke="#fcc419" stroke-width="4" fill="none" stroke-linecap="round"/>
    <!-- gears -->
    <circle cx="159" cy="227" r="21" fill="#fff" stroke="#1d5b73" stroke-width="1.5"/>
    <g fill="none" stroke="#1d5b73" stroke-width="2.5"><circle cx="153" cy="229" r="5"/><circle cx="164" cy="220" r="3.5"/><circle cx="165" cy="234" r="3.5"/></g>
    <!-- verify -->
    <circle cx="250" cy="227" r="21" fill="#fff" stroke="#4a8293" stroke-width="1.5"/>
    <circle cx="250" cy="227" r="14" fill="#4a8293"/><circle cx="250" cy="227" r="9" fill="#fff"/>
    <path d="M245 227l4 4 7-8" stroke="#4a8293" stroke-width="2.5" fill="none"/>
    <!-- optimize -->
    <circle cx="342" cy="227" r="21" fill="#fff" stroke="#5a5a5a" stroke-width="1.5"/>
    <circle cx="342" cy="227" r="14" fill="#5a5a5a"/><circle cx="342" cy="227" r="9" fill="#fff"/>
    <path d="M336 231l4-4 3 3 5-6M345 224h3v3" stroke="#5a5a5a" stroke-width="2" fill="none"/>
    <!-- repeat -->
    <circle cx="433" cy="227" r="21" fill="#fff" stroke="#222" stroke-width="1.5"/>
    <path d="M424 229a9 9 0 0 1 15-8M442 225a9 9 0 0 1-15 8" stroke="#222" stroke-width="3.5" fill="none"/>
    <path d="M436 217l6 3-4 5zM430 237l-6-3 4-5z" fill="#222"/>
  </svg>

  <div class="panel">
    <div class="panel__head">It’s easy to get going with Q-VARO...&nbsp;<span class="hl">All you have to do is:</span></div>
  </div>
  <div class="step-row" style="top:307px"><div class="step-row__num">1</div><svg width="26" height="78"><polygon points="0,0 16,0 26,39 16,78 0,78" fill="#1d5b73"/></svg><div class="step-row__text">Add your press lines into the software</div></div>
  <div class="step-row" style="top:397px"><div class="step-row__num">2</div><svg width="26" height="78"><polygon points="0,0 16,0 26,39 16,78 0,78" fill="#1d5b73"/></svg><div class="step-row__text">Complete a small study of on 3-5 projects to verify its capabilities</div></div>
  <div class="step-row" style="top:487px"><div class="step-row__num">3</div><svg width="26" height="78"><polygon points="0,0 16,0 26,39 16,78 0,78" fill="#1d5b73"/></svg><div class="step-row__text">Optimize all the projects in the press line</div></div>

  <div class="note">When you finished with your first press, repeat the process for the rest of them!</div>
  <div class="page__foot"></div>
</section>

<section class="page page--details">
  <div class="page__header">
    <div class="brand"><span class="brand__mark"></span><span class="brand__name">Q-VARO</span></div>
    <div class="title-band">Details of the Basic</div>
  </div>
  <div class="page__rule"></div>

  <div class="features">
    <div class="features__head">Key Features&nbsp;<span class="hl">and Benefits:</span></div>
    <ul class="features__list">
      <li>Optimize new AND existing tooling</li>
      <li>Optimize tooling with OR without&nbsp; CAD</li>
      <li>Full kinematic simulation(everything can be put in motion)</li>
      <li>Optimization without risk(lock your choke points)</li>
      <li>Proven system with 1000’s of simulation completed</li>
      <li>Full reporting capabilities(create corrective action reports, ppt, pdf, and tool launch packages)</li>
      <li>Video creation(show the simulation in real time-speed)</li>
      <li>Easy press change capabilities</li>
    </ul>
  </div>

  <div class="guarantee"><b>Guarantee:</b> We guarantee our software will pay for itself within the first (5) projects you us it on or we’ll refund you for the full purchase price!</div>
  <svg class="shield" width="56" height="64" viewBox="0 0 56 64">
    <path d="M28 1L54 12v18c0 17-12 28-26 33C14 58 2 47 2 30V12z" fill="#fff"/>
    <path d="M28 4L51 14v16c0 15-10 25-23 30C15 55 5 45 5 30V14z" fill="#fcc419"/>
    <path d="M16 31l9 9 16-18" stroke="#fff" stroke-width="5" fill="none"/>
  </svg>

  <div class="promise">You truly have nothing to loose!</div>
  <div class="contact-head">Contact&nbsp;<span class="hl">Us Today</span></div>
  <div class="contact-name">Q-VARO Solutions</div>
  <div class="contact-line" style="top:536px"><span class="contact-line__icon"><svg width="8" height="6"><path d="M0 0h8v6H0zM0 0l4 3 4-3" stroke="#fff" fill="none"/></svg></span>info@qvarosim.com</div>
  <div class="contact-line" style="top:554px"><span class="contact-line__icon"><svg width="8" height="8"><circle cx="4" cy="4" r="3.5" stroke="#fff" fill="none"/><path d="M0 4h8M4 0v8" stroke="#fff"/></svg></span>www.qvarosim.com</div>

  <div class="page__foot"></div>
</section>

</body>
</html>
```